Medical cannabis product (extract, e-cigarette, suppositories) packages

We are a small biotech company developing medical products based on cannabis. We are located in Israel. We need packages for 3 such products - liquid extracts, e-cigarette containing cannabis and cannabis suppositories. The packages are made of extreenal carton box and a sticker for extract bottle and e-cig. The labeling on the packages should be bi-lingual (hebrew and english), yet if the designer cannot put hebrew wording this is ok, as we can add them here.
The packages should look conservative and medicine like. It is important that the designs be as far as possible from the street cannabis graphic language.

pacakges blueprints are attached, also attached are the product pictures.

bottle label size is 5cm*10cm

Velodrix is the name of our company. Company logo should be on the label (uploaded with the other files).Product names are composed of the generic name, i.e. cannabis extract oil, cannabis electronic cigarette and cannabis suppositories and the THC\CBD strength in percentage.
The names that should appear on the boxes:
"Medical Cannabis Extract Oil, THC 15%"
"Medical Cannabis Electronic Cigarette, THC 10%"
""Medical Cannabis Suppositories, CBD 10%"

Also should be on the package the quantity that is in the box:
for the oil: 10ml, for the ecig: 50inhalations, 5mg each for the suppositories: 20 suppositories

Target Market(s)

Israel medical cannabis users, adults, no specific gender

Industry/Entity Type

Conservative

Requirements
Must have
• medicinal conservative look
Should not have
• graphic patterns that usually are connected with street cannabis terminology

```html
<!DOCTYPE html>
<html lang="en">
<head>
<meta charset="UTF-8">
<title>Velodrix – Medical Cannabis Suppositories</title>
<link rel="stylesheet" href="https://fonts.googleapis.com/css2?family=Roboto+Condensed:wght@400;700&display=swap">
<style>
  :root {
    --backdrop: #2f3331;
    --carton: #ddcfad;
    --carton-edge: #cbbd9a;
    --brand-red: #8c2a26;
    --rule-red: #9a3a34;
    --sage: #9eaea2;
    --leaf-tint: #c9cfbd;
    --ink: #4a4540;
  }
  * { box-sizing: border-box; margin: 0; padding: 0; }
  html, body {
    width: 1200px;
    height: 674px;
    overflow: hidden;
    background: var(--backdrop);
  }
  .canvas {
    position: relative;
    width: 1200px;
    height: 674px;
  }
  .box-front {
    position: absolute;
    left: 59px;
    top: 80px;
    width: 1082px;
    height: 514px;
    background: var(--carton);
    border-bottom: 3px solid var(--carton-edge);
    font-family: "Roboto Condensed", "Arial Narrow", sans-serif;
    overflow: hidden;
  }
  .leaf-art {
    position: absolute;
    left: 71px;
    top: 0;
    width: 411px;
    height: 198px;
    background: radial-gradient(ellipse at 50% 20%, var(--leaf-tint) 0%, rgba(201,207,189,0) 70%);
  }
  .brand-mark {
    position: absolute;
    left: 537px;
    top: 8px;
    width: 442px;
    height: 355px;
    display: flex;
    align-items: center;
    justify-content: center;
  }
  .brand-name {
    font-weight: 700;
    font-size: 96px;
    color: var(--sage);
    letter-spacing: 1px;
  }
  .product-title {
    position: absolute;
    left: 47px;
    top: 246px;
    color: var(--brand-red);
    font-weight: 700;
    text-transform: uppercase;
  }
  .product-title .generic {
    display: block;
    font-size: 60px;
    line-height: 54px;
  }
  .product-title .form {
    display: block;
    font-size: 33px;
    line-height: 38px;
    margin-top: 2px;
  }
  .rule {
    position: absolute;
    left: 0;
    right: 0;
    height: 2px;
    background: var(--rule-red);
  }
  .rule.r1 { top: 383px; }
  .rule.r2 { top: 389px; }
  .rule.r3 { top: 445px; }
  .rule.r4 { top: 480px; }
  .spec {
    position: absolute;
    left: 22px;
    font-size: 19px;
    color: var(--ink);
    line-height: 22px;
  }
  .spec.quantity { top: 418px; }
  .spec.dose { top: 454px; }
  .spec.strength { top: 488px; }
</style>
</head>
<body>
<main class="canvas">
  <section class="box-front">
    <div class="leaf-art" role="img" aria-label="Fine outline drawing of cannabis leaves"></div>

    <div class="brand-mark">
      <span class="brand-name">Velodrix</span>
    </div>

    <h1 class="product-title">
      <span class="generic">Medical</span>
      <span class="generic">Cannabis</span>
      <span class="form">Suppositories</span>
    </h1>

    <div class="rule r1"></div>
    <div class="rule r2"></div>
    <p class="spec quantity">20 suppositories</p>
    <div class="rule r3"></div>
    <p class="spec dose">5 mg</p>
    <div class="rule r4"></div>
    <p class="spec strength">CBD 10% medical cannabis</p>
  </section>
</main>
</body>
</html>
```